Design some Business Cards for Varno

Thanks to everyone for their efforts. I will just be reviewing the first two entries from each contestant, so I'd suggest withdrawing entries which are not your favorites & going with your best two. Many thanks, Gareth

I was after a double sided business card for varno.com.au. Varno is a billing app and website for tradesman and service providers who move from site to site.

Firstly design for Gareth Pimm with mobile 0412 555 806 & email demo@varno.com.au.

Logo is attached, so please work with those colours. I've also included our url if you believe that is worth building in.

I would like the original working files and the business card will need to be produced for 3 different employees when the winner is selected.

Additional VARNO text files if this helps.

```html
<!DOCTYPE html>
<html lang="en">
<head>
<meta charset="utf-8">
<title>Varno Business Cards</title>
<link rel="stylesheet" href="https://fonts.googleapis.com/css2?family=Arimo:wght@400;700&display=swap">
<style>
  :root {
    --page-bg: #ece9e4;
    --card-bg: #ffffff;
    --ink: #1f1f1f;
    --brand-grey: #3a3a3c;
    --brand-red: #d8322b;
    --brand-blue: #2f5fc4;
    --card-shadow: rgba(0, 0, 0, 0.16);
  }
  * { box-sizing: border-box; margin: 0; padding: 0; }
  html, body {
    width: 1200px;
    height: 912px;
    overflow: hidden;
    background: var(--page-bg);
    font-family: "Arimo", Arial, sans-serif;
  }
  .sheet {
    position: relative;
    width: 1200px;
    height: 912px;
  }
  .card {
    position: absolute;
    width: 525px;
    height: 300px;
    background: var(--card-bg);
    box-shadow: 0 6px 18px var(--card-shadow);
  }
  .card--front { left: 45px; top: 230px; }
  .card--back  { left: 630px; top: 382px; }

  .brand {
    position: absolute;
    display: flex;
    align-items: center;
  }
  .brand-dot {
    border-radius: 50%;
    background: var(--brand-blue);
    flex: none;
  }
  .brand-name {
    color: var(--brand-grey);
    font-weight: 700;
    letter-spacing: 0.08em;
    line-height: 1;
  }

  .card--front .brand { left: 110px; top: 58px; gap: 18px; }
  .card--front .brand-dot { width: 52px; height: 52px; }
  .card--front .brand-name { font-size: 50px; }

  .contact {
    position: absolute;
    left: 0;
    right: 0;
    top: 148px;
    text-align: center;
    color: var(--ink);
    font-size: 15px;
    line-height: 1.45;
  }
  .contact-name {
    color: var(--brand-red);
    font-size: 17px;
    margin-bottom: 8px;
  }

  .card--back .brand { left: 58px; top: 88px; gap: 26px; }
  .card--back .brand-dot { width: 84px; height: 84px; }
  .card--back .brand-name { font-size: 76px; }

  .web {
    position: absolute;
    left: 0;
    right: 0;
    bottom: 46px;
    text-align: center;
    color: var(--ink);
    font-size: 15px;
  }
  .web-accent { color: var(--brand-red); }
</style>
</head>
<body>
  <main class="sheet">
    <section class="card card--front" aria-label="Business card front">
      <div class="brand">
        <span class="brand-dot"></span>
        <span class="brand-name">VARNO</span>
      </div>
      <div class="contact">
        <p class="contact-name">Gareth Pimm</p>
        <p class="contact-phone">0412 555 806</p>
        <p class="contact-email">demo@varno.com.au</p>
        <p class="contact-web">www.varno.com.au</p>
      </div>
    </section>

    <section class="card card--back" aria-label="Business card back">
      <div class="brand">
        <span class="brand-dot"></span>
        <span class="brand-name">VARNO</span>
      </div>
      <p class="web">www.<span class="web-accent">varno</span>.com.au</p>
    </section>
  </main>
</body>
</html>
```